QVAR Individual and Corporate Development Business Card Design

QVAR needs a business card design that is aligned with it's values and targetted markets. Harmonic Lattice of Cognition Network's self diagnosis model and tools, which can be used for personal improvement and team/business performance enhancement, is based on the learnings of over 20 years of medical practitioning. QVAR supercharges personal effectiveness and awareness to also increase team and business performance.

The targetted markets are high performance individuals and teams who aspire seek to enhance their capabilities and achieve their absolute best potential.

Look and feel for the business card design we are looking for is high technology, premium, fresh, new and medical.

Target Market(s)

Industry/Entity Type

Business Consultant

Contact Information for Business Card

Logo, Full Name, Title, Phone number, Email, company name, Address,

Font styles to use
Sans Serif

Requirements
Must have
• Tag line: Maximising Performance for Highly Effective People
• Please use same colours as the logo.

```html
<!DOCTYPE html>
<html lang="en">
<head>
<meta charset="utf-8">
<title>QVAR Business Card</title>
<link rel="stylesheet" href="https://fonts.googleapis.com/css2?family=Roboto:wght@300;400;500;700&display=swap">
<style>
  :root {
    --page: #e9e7e4;
    --card: #eef1f2;
    --card-edge: #d7dcde;
    --teal: #1f7f8c;
    --teal-deep: #0f6577;
    --teal-soft: rgba(31,127,140,0.12);
    --teal-mid: rgba(31,127,140,0.6);
    --ink: #2e3438;
    --charcoal: #3c3d40;
    --on-teal: #f1e6d8;
  }
  * { margin: 0; padding: 0; box-sizing: border-box; }
  html, body { width: 1200px; height: 970px; overflow: hidden; }
  body {
    background: var(--page);
    font-family: "Roboto", Arial, sans-serif;
    display: flex; align-items: center; justify-content: center;
  }
  .business-card {
    position: relative;
    width: 1000px; height: 568px;
    border-radius: 32px;
    background: linear-gradient(160deg, #f6f8f9 0%, var(--card) 55%, #e3e8ea 100%);
    border: 1px solid var(--card-edge);
    box-shadow: 0 18px 40px rgba(0,0,0,0.15);
    overflow: hidden;
  }
  .wave-band {
    position: absolute; left: 0; right: 0; bottom: 0; height: 250px;
    background: linear-gradient(100deg, var(--teal-soft) 0%, var(--teal-mid) 38%, var(--teal) 58%, var(--teal-deep) 100%);
  }
  .brand {
    position: absolute; left: 92px; top: 92px;
    color: var(--teal);
  }
  .brand-name {
    display: flex; align-items: center; gap: 18px;
    font-weight: 700; font-size: 88px; line-height: 1; letter-spacing: 4px;
  }
  .brand-dot { width: 24px; height: 24px; border-radius: 50%; background: var(--teal); }
  .brand-rule { width: 410px; height: 2px; background: #8d9599; margin: 14px 0 10px -40px; }
  .brand-full {
    font-weight: 500; font-size: 23px; line-height: 1.1; letter-spacing: 0.5px;
    text-transform: uppercase; width: 380px;
  }
  .tagline {
    margin-top: 12px; width: 470px;
    color: var(--charcoal); font-weight: 400; font-size: 17px; line-height: 1.2;
  }
  .holder { position: absolute; right: 48px; top: 70px; text-align: right; }
  .holder-name { color: var(--teal-deep); font-weight: 500; font-size: 30px; text-transform: uppercase; }
  .holder-title { color: var(--ink); font-size: 23px; }
  .contact {
    position: absolute; right: 48px; top: 340px; text-align: right;
    color: var(--on-teal); font-weight: 300; font-size: 23px; line-height: 33px;
  }
  .address { margin-bottom: 28px; }
  .contact-line { display: flex; justify-content: flex-end; align-items: center; gap: 12px; height: 35px; }
  .contact-icon { width: 28px; height: 28px; flex: none; }
</style>
</head>
<body>
  <article class="business-card">
    <div class="wave-band" role="img" aria-label="Flowing teal, charcoal and blush wave decoration across the lower card"></div>

    <div class="brand">
      <div class="brand-name"><span>QVAR</span><span class="brand-dot"></span></div>
      <div class="brand-rule"></div>
      <div class="brand-full">Harmonic Lattice of Cognition Network</div>
      <div class="tagline">Maximising Performance for Highly Effective People</div>
    </div>

    <div class="holder">
      <div class="holder-name">Owen Barlow</div>
      <div class="holder-title">Founder</div>
    </div>

    <div class="contact">
      <div class="address">PO BOX 418 Wattle Lane<br>7th street Geelong</div>
      <div class="contact-line">(555) 204-3817
        <svg class="contact-icon" viewBox="0 0 28 28" aria-hidden="true"><circle cx="14" cy="14" r="12.5" fill="none" stroke="currentColor" stroke-width="1.5"/><rect x="10" y="7" width="8" height="14" rx="1.5" fill="none" stroke="currentColor" stroke-width="1.5"/></svg>
      </div>
      <div class="contact-line">hello@qvarmail.com
        <svg class="contact-icon" viewBox="0 0 28 28" aria-hidden="true"><circle cx="14" cy="14" r="12.5" fill="none" stroke="currentColor" stroke-width="1.5"/><rect x="8" y="9.5" width="12" height="9" fill="none" stroke="currentColor" stroke-width="1.5"/><path d="M8 9.5 L14 15 L20 9.5" fill="none" stroke="currentColor" stroke-width="1.5"/></svg>
      </div>
      <div class="contact-line">www.qvarnetwork.com
        <svg class="contact-icon" viewBox="0 0 28 28" aria-hidden="true"><circle cx="14" cy="14" r="12.5" fill="none" stroke="currentColor" stroke-width="1.5"/><circle cx="14" cy="14" r="7" fill="none" stroke="currentColor" stroke-width="1.3"/><ellipse cx="14" cy="14" rx="3" ry="7" fill="none" stroke="currentColor" stroke-width="1.2"/><path d="M7 14 H21" stroke="currentColor" stroke-width="1.2"/></svg>
      </div>
    </div>
  </article>
</body>
</html>
```